Civic Counsel and Advocacy Network needs poster design for landlord/tenant cases

We're seeking a poster design (11x17) to spread awareness for services by "Civic Counsel and Advocacy Network". The services they're trying to communicate are regarding housing/landlord/tenant matters.

We'd like the poster to (1) reflect the color scheme and branding of their website www.ccanplumridge.org, (2) contain the following copy: "Everyone needs safe and suitable housing, whether they own a home or rent one. When homelessness threatens, we at CCN help clients free of charge through eviction diversion programs and mortgage/tax foreclosure prevention.", and (3) contain their contact information:

Civic Counsel and Advocacy Network, Inc.
"We are YOUR Law Firm for Housing matters"
Contact us at: (555) 314-6082
housing @ccanplumridge.org
www.ccanplumridge.org

Target Market(s)

People who may be facing eviction or homelessness

Industry/Entity Type

Legal

Colors
0054AA
0677BA
7BADD7
CADEEF
E8F1F8
FFC000
F8CF3A
FAE287
FDF2CF
FEFAEE
EB3D1F
EC4F4E
F09395
F8D3D4
FCEDEE

Requirements
Must have
• Must include colors from website: https://ccanplumridge.org/

```html
<!DOCTYPE html>
<html lang="en">
<head>
<meta charset="utf-8">
<title>Civic Counsel and Advocacy Network — Housing Matters</title>
<link href="https://fonts.googleapis.com/css2?family=Cinzel:wght@700;800&family=Work+Sans:wght@500;600&display=swap" rel="stylesheet">
<style>
  :root {
    --navy: #1f2a5c;
    --house-top: #3a4a78;
    --house-mid: #41507d;
    --house-bottom: #2a3766;
    --gold: #e0aa33;
    --coral: #ec6f50;
    --white: #ffffff;
    --footer-bg: #f0f0f2;
    --ink: #1c1c22;
    --photo-warm: #b98a74;
    --photo-warm-deep: #9c7264;
  }
  * { margin: 0; padding: 0; box-sizing: border-box; }
  html, body { width: 776px; height: 1200px; overflow: hidden; background: var(--white); }
  .poster {
    position: relative;
    width: 776px;
    height: 1200px;
    background: var(--navy);
    overflow: hidden;
    font-family: "Work Sans", Arial, sans-serif;
  }
  .house-photo {
    position: absolute;
    left: 0; top: 0;
    width: 776px; height: 510px;
    background: linear-gradient(180deg, var(--house-top) 0%, var(--house-mid) 55%, var(--house-bottom) 100%);
  }
  .sun-circle {
    position: absolute;
    left: 385px; top: 410px;
    width: 350px; height: 500px;
  }
  .hands-photo {
    position: absolute;
    left: 395px; top: 0;
    width: 335px; height: 1045px;
    background: linear-gradient(180deg, var(--photo-warm) 0%, var(--photo-warm-deep) 100%);
    opacity: 0.85;
  }
  .headline {
    position: absolute;
    left: 70px; top: 138px;
    font-family: "Cinzel", Georgia, serif;
    font-weight: 800;
    font-size: 56px;
    line-height: 69px;
    text-transform: uppercase;
    color: var(--white);
    text-shadow: 3px 3px 0 rgba(10, 14, 40, 0.65);
  }
  .headline .accent-gold { color: var(--gold); }
  .headline .accent-coral { color: var(--coral); }
  .quote-mark {
    position: absolute;
    left: 68px; top: 560px;
    font-family: "Cinzel", Georgia, serif;
    font-weight: 700;
    font-size: 120px;
    line-height: 1;
    color: var(--coral);
  }
  .mission {
    position: absolute;
    left: 73px; top: 662px;
    width: 212px;
    font-weight: 600;
    font-size: 16px;
    line-height: 25.3px;
    color: var(--white);
  }
  .side-credit {
    position: absolute;
    left: 725px; top: 1000px;
    transform: rotate(-90deg);
    transform-origin: left top;
    white-space: nowrap;
    font-size: 12px;
    font-weight: 500;
    color: var(--white);
  }
  .footer {
    position: absolute;
    left: 0; top: 1046px;
    width: 776px; height: 154px;
    background: var(--footer-bg);
  }
  .brand {
    position: absolute;
    left: 63px; top: 46px;
    display: flex;
    align-items: center;
    gap: 18px;
  }
  .brand-dot {
    width: 62px; height: 62px;
    border-radius: 50%;
    background: var(--ink);
  }
  .brand-name {
    width: 260px;
    font-family: "Cinzel", Georgia, serif;
    font-weight: 700;
    font-size: 14px;
    line-height: 18px;
    text-transform: uppercase;
    color: var(--ink);
  }
  .divider {
    position: absolute;
    left: 445px; top: 44px;
    width: 1.5px; height: 72px;
    background: var(--ink);
  }
  .contact {
    position: absolute;
    left: 488px; top: 54px;
    list-style: none;
    font-weight: 500;
    font-size: 16px;
    line-height: 22px;
    letter-spacing: 0.6px;
    color: var(--ink);
  }
</style>
</head>
<body>
<main class="poster">
  <div class="house-photo" role="img" aria-label="Photo of a two-storey suburban house at dusk"></div>

  <svg class="sun-circle" viewBox="0 0 350 500" aria-hidden="true">
    <ellipse cx="185" cy="250" rx="160" ry="225" fill="#e0aa33"/>
  </svg>

  <div class="hands-photo" role="img" aria-label="Photo of one hand reaching down to help another hand up"></div>

  <h1 class="headline">
    We are<br>
    <span class="accent-gold">your</span> law firm<br>
    for <span class="accent-coral">housing</span><br>
    <span class="accent-coral">matters</span>
  </h1>

  <div class="quote-mark" aria-hidden="true">&ldquo;</div>
  <p class="mission">Everyone needs safe and affordable housing, whether they own a home or rent one. When homelessness threatens, we at CCN help clients free of charge through eviction diversion programs and mortgage/tax foreclosure prevention.</p>

  <p class="side-credit">Civic Counsel and Advocacy Network, Inc.</p>

  <footer class="footer">
    <div class="brand">
      <span class="brand-dot" aria-hidden="true"></span>
      <span class="brand-name">Civic Counsel and Advocacy Network Incorporated</span>
    </div>
    <span class="divider" aria-hidden="true"></span>
    <ul class="contact">
      <li>(555) 314-6082</li>
      <li>housing @ccanplumridge.org</li>
      <li>www.ccanplumridge.org</li>
    </ul>
  </footer>
</main>
</body>
</html>
```